Brightmoor Law Letterhead for Law firm must be modern and use the logo I uploaded.

Hello I want a clean modern professional letterhead for my law firm Brightmoor Law. A logo has already been created and all files have been uploaded. The information for the firm can be given through message. Please use the logo that has already been created. Please also use the color scheme of that logo. (blue and white).

Target Market(s)

General Public

Industry/Entity Type

Law Firm

Colors

Designer to choose colors to be used in the design.

Requirements
Must have
• This must be a modern professional letterhead
Nice to have
• My logo that is included in file form
Should not have
• Should not have logo that is not the one I uploaded.

```html
<!DOCTYPE html>
<html lang="en">
<head>
<meta charset="utf-8">
<title>Brightmoor Law Letterhead</title>
<link rel="stylesheet" href="https://fonts.googleapis.com/css2?family=Heebo:wght@300;400;500;700&display=swap">
<style>
  :root {
    --backdrop: #a9afac;
    --paper: #f1f1f1;
    --navy: #262a5c;
    --ink: #6a6a6a;
    --ink-dark: #3a3a3a;
    --white: #ffffff;
    --sign-tone: #e4e4e4;
  }
  * { margin: 0; padding: 0; box-sizing: border-box; }
  html, body { width: 1200px; height: 803px; overflow: hidden; }
  body {
    background: var(--backdrop);
    font-family: "Heebo", Arial, sans-serif;
    position: relative;
  }
  .letterhead {
    position: absolute;
    left: 330px; top: 21px;
    width: 541px; height: 761px;
    background: var(--paper);
    overflow: hidden;
  }
  .brand {
    position: absolute;
    left: 51px; top: 92px;
    display: flex; align-items: center; gap: 8px;
  }
  .brand-square { width: 9px; height: 9px; background: var(--navy); }
  .brand-name {
    font-size: 11px; font-weight: 500; color: var(--navy);
    letter-spacing: 0.3em; text-transform: uppercase;
  }
  .contact {
    position: absolute;
    left: 317px; top: 91px;
    display: flex; gap: 8px;
    font-size: 6.5px; line-height: 10px; font-weight: 400; color: var(--ink-dark);
  }
  .contact-divider { width: 1px; background: var(--ink-dark); height: 20px; }
  .contact-row { display: flex; align-items: center; gap: 3px; }
  .contact-row svg { width: 5px; height: 5px; fill: var(--navy); }
  .date {
    position: absolute; right: 51px; top: 188px;
    font-size: 10px; font-weight: 300; color: var(--ink);
  }
  .letter-body {
    position: absolute; left: 46px; top: 213px; width: 443px;
    font-size: 10.4px; line-height: 15.2px; font-weight: 300; color: var(--ink);
  }
  .salutation { margin-bottom: 21px; font-size: 10px; }
  .letter-body p.para { text-align: justify; margin-bottom: 22px; }
  .letter-body p.para + p.para + p.para { margin-top: 3px; }
  .signature {
    position: absolute; left: 42px; top: 584px;
    width: 99px; height: 59px; background: var(--sign-tone);
  }
  .footer-band {
    position: absolute; left: 0; top: 720px;
    width: 100%; height: 22px; background: var(--navy);
  }
  .footer-web {
    position: absolute; right: 34px; top: 6px;
    font-size: 8px; line-height: 10px; color: var(--white); letter-spacing: 0.05em;
  }
  .footer-web b { font-weight: 700; }
  .footer-web span { font-weight: 300; }
</style>
</head>
<body>
  <main class="letterhead">
    <header>
      <div class="brand">
        <div class="brand-square"></div>
        <div class="brand-name">Brightmoor Law</div>
      </div>
      <div class="contact">
        <div class="contact-address">Harrow Lane North<br>Elmstead NSW 2150</div>
        <div class="contact-divider"></div>
        <div class="contact-lines">
          <div class="contact-row">
            <svg viewBox="0 0 10 10"><path d="M2 0h2l1 3-1.5 1a6 6 0 0 0 2.5 2.5L7 5l3 1v2a2 2 0 0 1-2 2A8 8 0 0 1 0 2a2 2 0 0 1 2-2z"/></svg>
            1300 52 61 47
          </div>
          <div class="contact-row">
            <svg viewBox="0 0 10 10"><path d="M0 2h10v6H0z"/></svg>
            contact@brightmoorlaw.com
          </div>
        </div>
      </div>
    </header>

    <div class="date">Dated: February 15, 2023</div>

    <section class="letter-body">
      <p class="salutation">Dear Sir,</p>
      <p class="para">Lorem Ipsum is simply dummy text of the printing and typesetting industry. Lorem Ipsum has been the industry's standard dummy text ever since the 1500s, when an unknown printer took a galley of type and scrambled it to make a type specimen book. It has survived not only five centuries, but also the leap into electronic typesetting, remaining essentially unchanged. It was popularised in the 1960s with the release of Typeline sheets containing Lorem Ipsum passages, and more recently with desktop publishing software like Folio Layout including versions of Lorem Ipsum.</p>
      <p class="para">It is a long established fact that a reader will be distracted by the readable content of a page when looking at its layout. The point of using Lorem Ipsum is that it has a more-or-less normal distribution of letters, as opposed to using 'Content here, content here', making it look like readable English. Many desktop publishing packages and web page editors now use Lorem Ipsum as their default model text, and a search for 'lorem ipsum' will uncover many web sites still in their infancy. Various versions have evolved over the years, sometimes by accident, sometimes on purpose (injected humour and the like).</p>
      <p class="para">The standard chunk of Lorem Ipsum used since the 1500s is reproduced below for those interested. Sections 1.10.32 and 1.10.33 from "de Finibus Bonorum et Malorum" by Aurelian Voss are also reproduced in their exact original form, accompanied by English versions from the 1914 translation by J. Holloway.</p>
    </section>

    <div class="signature" role="img" aria-label="Handwritten signature of the sender"></div>

    <footer class="footer-band">
      <div class="footer-web"><b>brightmoorlaw</b><span>.com</span></div>
    </footer>
  </main>
</body>
</html>
```